NEW Modern Sleek Business Card for VR Language Startup

Our startup is using VR to lead the next wave of world language education. We need a two-sided business card that introduces the larger organization (Quorvel Language Inc) and our contact info on one side and shows the product, Lumidrasca, on the other side.

Side 1 (contact info)= Quorvel Logo and Contact info (name, title, phone, email)

Side 2 (product)= Lumidrasc logo, text, and website
Text= Culturally Immersive Language Learning Games
Website= www.lumidrasc.example

Target Market(s)

Education, Technology

Contact Information for Business Card

Contact info will be updated upon approval of the design. For now, put this as a placeholder.

Perry Hollins
Founder & CEO
phollins@mailtrove.example
(555)-014-2736

Font styles to use
Other font styles liked:
• Gibson and Century Gothic are the brand fonts

Requirements
Nice to have
• I would love to see cohesion between the design and colors of the two logos. I have attached a few business card designs that I like, so you can get a feel for my preferred style.

```html
<!DOCTYPE html>
<html lang="en">
<head>
<meta charset="utf-8">
<title>Quorvel Language – Business Card</title>
<link href="https://fonts.googleapis.com/css2?family=Questrial&family=Montserrat:wght@500;600&display=swap" rel="stylesheet">
<style>
  :root {
    --stage: #e7e2da;
    --ink: #262626;
    --white: #ffffff;
    --red: #e5283c;
    --blue: #4652b4;
    --sky: #4fb4e6;
    --orange: #f28a32;
    --yellow: #f3e64b;
    --night: #0c0c0e;
    --sans: "Questrial", "Century Gothic", sans-serif;
    --display: "Montserrat", "Century Gothic", sans-serif;
  }
  * { box-sizing: border-box; margin: 0; padding: 0; }
  html, body { width: 900px; height: 1200px; overflow: hidden; }
  body { background: var(--stage); position: relative; font-family: var(--sans); }

  .card {
    position: absolute; left: 80px; width: 735px; height: 429px;
    border-radius: 22px; overflow: hidden;
    box-shadow: 0 8px 22px rgba(0,0,0,.28);
  }
  .card svg.art { position: absolute; inset: 0; }

  /* Front: company + contact */
  .card--front { top: 128px; background: linear-gradient(180deg, #fff 0%, #fff 30%, #d9eef8 55%); }
  .brand { position: absolute; left: 50px; top: 52px; display: flex; align-items: center; gap: 18px; }
  .brand__dot { width: 96px; height: 96px; border-radius: 50%; background: var(--red); }
  .brand__name { color: var(--ink); font-family: var(--display); font-weight: 500; line-height: 1; }
  .brand__name .main { display: block; font-size: 54px; letter-spacing: 6px; }
  .brand__name .sub { display: block; font-size: 22px; letter-spacing: 9px; margin-top: 8px; padding-left: 10px; }

  .person { position: absolute; left: 48px; top: 322px; color: var(--white); }
  .person__name { font-family: var(--display); font-weight: 600; font-size: 25px; }
  .person__title { font-size: 18px; color: var(--yellow); margin-top: 4px; }

  .contact { position: absolute; right: 30px; top: 324px; color: var(--white); font-size: 19px; text-align: right; }
  .contact li { list-style: none; display: flex; align-items: center; justify-content: flex-end; gap: 10px; height: 29px; }
  .contact .icon { width: 22px; height: 22px; }

  /* Back: product */
  .card--back { top: 645px; background: radial-gradient(ellipse at 55% 40%, #26262b 0%, var(--night) 65%); }
  .product { position: absolute; left: 0; right: 0; top: 72px; text-align: center; color: var(--white); }
  .product__dot { width: 120px; height: 120px; border-radius: 50%; background: var(--sky); margin: 0 auto 38px; }
  .product__name { font-size: 56px; line-height: 1; }
  .product__tagline { font-size: 21px; margin-top: 14px; }
  .web-band {
    position: absolute; left: 0; right: 0; top: 367px; height: 37px;
    background: linear-gradient(90deg, var(--sky) 0%, #6a62c4 40%, #c96a7a 70%, var(--orange) 100%);
    color: var(--white); font-size: 23px; letter-spacing: 6px;
    display: flex; align-items: center; justify-content: center;
  }
</style>
</head>
<body>

<section class="card card--front">
  <svg class="art" width="735" height="429" viewBox="0 0 735 429">
    <defs>
      <linearGradient id="bandFill" x1="0" y1="0" x2="0" y2="1">
        <stop offset="0" stop-color="var(--red)"/>
        <stop offset="0.45" stop-color="#c23a6a"/>
        <stop offset="1" stop-color="var(--blue)"/>
      </linearGradient>
    </defs>
    <path role="img" aria-label="Circuit-trace pattern on colour band"
          d="M0 228 C 160 260, 330 240, 470 200 C 570 172, 650 178, 735 222 L735 429 L0 429 Z"
          fill="url(#bandFill)"/>
    <path d="M0 208 C 160 248, 330 228, 470 188 C 570 160, 650 166, 735 210"
          fill="none" stroke="var(--white)" stroke-width="16"/>
    <!-- accent lines -->
    <g fill="none" stroke-width="4">
      <line x1="563" y1="70" x2="735" y2="70" stroke="var(--orange)"/>
      <circle cx="555" cy="70" r="8" stroke="var(--orange)"/>
      <line x1="515" y1="101" x2="735" y2="101" stroke="var(--blue)"/>
      <circle cx="507" cy="101" r="8" stroke="var(--blue)"/>
      <line x1="617" y1="131" x2="735" y2="131" stroke="var(--red)"/>
      <circle cx="609" cy="131" r="8" stroke="var(--red)"/>
    </g>
    <!-- divider -->
    <g stroke="var(--white)" fill="none" stroke-width="1.5">
      <line x1="48" y1="310" x2="326" y2="310"/>
      <circle cx="332" cy="310" r="5"/>
      <circle cx="351" cy="310" r="5"/>
      <line x1="357" y1="310" x2="685" y2="310"/>
    </g>
  </svg>

  <div class="brand">
    <span class="brand__dot"></span>
    <span class="brand__name"><span class="main">QUORVEL</span><span class="sub">LANGUAGE</span></span>
  </div>

  <div class="person">
    <p class="person__name">PERRY HOLLINS</p>
    <p class="person__title">CEO/FOUNDER</p>
  </div>

  <ul class="contact">
    <li>555-014-2736
      <svg class="icon" viewBox="0 0 22 22"><circle cx="11" cy="11" r="10" fill="var(--orange)" stroke="#fff" stroke-width="1.5"/><path d="M7.5 6.5l2 0 1 2.5-1.3 1c.6 1.3 1.5 2.2 2.8 2.8l1-1.3 2.5 1v2c-4.5.3-8.3-3.5-8-8z" fill="#fff"/></svg>
    </li>
    <li>phollins@mailtrove.example
      <svg class="icon" viewBox="0 0 22 22"><circle cx="11" cy="11" r="10" fill="var(--orange)" stroke="#fff" stroke-width="1.5"/><rect x="6" y="7.5" width="10" height="7" fill="#fff"/><path d="M6 7.5l5 4 5-4" fill="none" stroke="var(--orange)" stroke-width="1.2"/></svg>
    </li>
  </ul>
</section>

<section class="card card--back">
  <svg class="art" width="735" height="429" viewBox="0 0 735 429">
    <defs>
      <radialGradient id="traceGlow" cx="0.5" cy="0.35" r="0.6">
        <stop offset="0" stop-color="#3a3a40" stop-opacity="0.55"/>
        <stop offset="1" stop-color="#0c0c0e" stop-opacity="0"/>
      </radialGradient>
    </defs>
    <rect role="img" aria-label="Faint circuit-trace background pattern" width="735" height="367" fill="url(#traceGlow)"/>
  </svg>
  <div class="product">
    <div class="product__dot"></div>
    <p class="product__name">Lumidrasc</p>
    <p class="product__tagline">Culturally Immersive Language Learning Games</p>
  </div>
  <div class="web-band">WWW.LUMIDRASC.EXAMPLE</div>
</section>

</body>
</html>
```